Kettle Ledger Business Card design

We need a stand out business card design for Accounting practice based in Australia specialising in pubs, clubs and hotels. We help venues maximise margins, create time and manage cashflow. One club we have been working with for the last 6 months has increased revenue by 3% and margin by 5% in this time frame. We have a back office outsourced system that costs less than having a full time employee and also allows the venues the added benefit of:<br/>-using the office space to become a revenue generating opportunity. <br/>-a complete system to enhance governance, accountability and efficiency within their operation<br/>-52 weeks cover so no hassle to cover annual/sick .. leave<br/><br/>We would like to see designs that use the colours of our logo (green & blue).
Target Market(s)
Australian Pubs, Clubs & Hotels abookkeeping, accounting and tax services
Industry/Entity Type
Accountant
Contact Information for Business Card
Miriam Oakley CPA
Principal
Accountant Tax Agent
Miriam@KettleLedger-example.com.au
0418693142
www.kettleledger-example.com.au
Accounting / Payroll / Tax / SMSF / Technology
Colors
Designer to choose colors to be used in the design.
Look and feel
Each slider illustrates characteristics of the customer's brand and the style your logo design should communicate.

```html
<!DOCTYPE html>
<html lang="en">
<head>
<meta charset="UTF-8">
<title>Kettle Ledger Business Card</title>
<link rel="stylesheet" href="https://fonts.googleapis.com/css2?family=Poppins:wght@400;500;700&display=swap">
<style>
  :root {
    --ground: #2b2b2b;
    --brand-green: #1a7a3c;
    --brand-blue: #1f3a93;
    --paper: #f4f5f3;
    --ink-grey: #3d3d3d;
    --ghost: #e3e9e6;
    --white: #ffffff;
  }
  * { box-sizing: border-box; margin: 0; padding: 0; }
  html, body {
    width: 1200px; height: 900px; overflow: hidden;
    background: var(--ground);
    font-family: "Poppins", sans-serif;
  }
  .stage { position: relative; width: 1200px; height: 900px; }

  .card {
    position: absolute; left: 320px; width: 560px; height: 320px;
    box-shadow: 0 10px 24px rgba(0,0,0,0.45);
    overflow: hidden;
  }

  /* front */
  .card-front { top: 90px; background: var(--brand-green); color: var(--white); }
  .front-brand {
    position: absolute; left: 0; right: 0; top: 112px;
    display: flex; justify-content: center; align-items: center; gap: 14px;
  }
  .brand-dot {
    width: 22px; height: 22px; border-radius: 50%;
    border: 3px solid currentColor;
  }
  .brand-name { font-weight: 700; font-size: 46px; letter-spacing: -0.5px; line-height: 1; }
  .front-services {
    position: absolute; left: 0; right: 0; bottom: 34px;
    text-align: center; font-size: 11px; letter-spacing: 1.6px; font-weight: 400;
  }

  /* back */
  .card-back { top: 470px; background: var(--paper); }
  .back-brand {
    position: absolute; right: 40px; top: 40px;
    display: flex; align-items: center; gap: 10px; color: var(--brand-blue);
  }
  .back-brand .brand-name { font-size: 28px; }
  .back-brand .brand-dot { width: 16px; height: 16px; border-width: 2.5px; border-color: var(--brand-green); }
  .rule { position: absolute; height: 1px; background: var(--brand-blue); }
  .rule-top { left: 230px; right: 40px; top: 122px; }
  .rule-mid { left: 40px; width: 250px; top: 222px; }
  .backdrop-motif {
    position: absolute; left: 50px; top: 70px; width: 230px; height: 240px;
    border-radius: 48% 48% 44% 44%;
    background: radial-gradient(circle at 50% 40%, var(--ghost), rgba(227,233,230,0.2));
  }
  .holder { position: absolute; left: 40px; top: 168px; }
  .holder-name { font-weight: 700; font-size: 20px; color: var(--brand-blue); line-height: 1.1; }
  .holder-role { font-weight: 500; font-size: 13px; color: var(--brand-green); margin-top: 3px; }
  .contacts { position: absolute; left: 40px; top: 234px; list-style: none; }
  .contacts li {
    display: flex; align-items: center; gap: 8px;
    font-size: 12.5px; color: var(--ink-grey); line-height: 20px;
  }
  .contacts svg { width: 11px; height: 11px; fill: var(--brand-blue); flex: none; }
</style>
</head>
<body>
<main class="stage">
  <section class="card card-front">
    <div class="front-brand">
      <span class="brand-dot"></span>
      <span class="brand-name">Kettle Ledger</span>
    </div>
    <p class="front-services">ACCOUNTING • PAYROLL • TAX • SMSF • TECHNOLOGY</p>
  </section>

  <section class="card card-back">
    <div class="backdrop-motif" role="img" aria-label="Large faint brand emblem watermark"></div>
    <div class="back-brand">
      <span class="brand-dot"></span>
      <span class="brand-name">Kettle Ledger</span>
    </div>
    <div class="rule rule-top"></div>
    <div class="holder">
      <h1 class="holder-name">Miriam Oakley CPA</h1>
      <p class="holder-role">Principal | Accountant Tax Agent</p>
    </div>
    <div class="rule rule-mid"></div>
    <ul class="contacts">
      <li>
        <svg viewBox="0 0 24 24" aria-hidden="true"><path d="M6.6 10.8a15.1 15.1 0 0 0 6.6 6.6l2.2-2.2a1 1 0 0 1 1-.25 11.4 11.4 0 0 0 3.6.57 1 1 0 0 1 1 1V20a1 1 0 0 1-1 1A17 17 0 0 1 3 4a1 1 0 0 1 1-1h3.5a1 1 0 0 1 1 1c0 1.25.2 2.45.57 3.6a1 1 0 0 1-.25 1z"/></svg>
        0418693142
      </li>
      <li>
        <svg viewBox="0 0 24 24" aria-hidden="true"><path d="M2 5h20v14H2z M2 5l10 7 10-7" /></svg>
        Miriam@KettleLedger-example.com.au
      </li>
      <li>
        <svg viewBox="0 0 24 24" aria-hidden="true"><circle cx="12" cy="12" r="10"/></svg>
        www.kettleledger-example.com.au
      </li>
    </ul>
  </section>
</main>
</body>
</html>
```